Business Card Project

We are a small consulting firm. You can experiment with any design.
Must have:
1) Company name - TOLVIN International
2) Company slogan - simple solutions for complex problems
3) Name/Title/Phone/Email/WWW/ - use anything you like as an example.

Industry/Entity Type

Business

```html
<!DOCTYPE html>
<html lang="en">
<head>
<meta charset="utf-8">
<title>TOLVIN International – Business Card</title>
<link href="https://fonts.googleapis.com/css2?family=Exo+2:wght@400;600;700&display=swap" rel="stylesheet">
<style>
  :root {
    --stage: #2b2b2d;
    --front-blue: #00a9ec;
    --front-blue-deep: #0096d8;
    --front-glow: #bfe9fa;
    --front-text: #dff4fd;
    --back-light: #b3e3f8;
    --back-mid: #9fd9f4;
    --accent-blue: #1a9fe0;
    --ink: #3d4146;
  }
  * { box-sizing: border-box; margin: 0; padding: 0; }
  html, body { width: 1200px; height: 900px; overflow: hidden; }
  body {
    background: var(--stage);
    font-family: "Exo 2", sans-serif;
    position: relative;
  }
  .card {
    position: absolute;
    left: 290px;
    width: 620px;
    height: 354px;
    overflow: hidden;
    box-shadow: 0 10px 30px rgba(0,0,0,.45);
  }
  /* Front side */
  .card--front {
    top: 76px;
    background: linear-gradient(135deg, var(--front-blue) 0%, var(--front-blue-deep) 100%);
  }
  .front-glow {
    position: absolute;
    inset: 0;
    background: linear-gradient(100deg, var(--front-glow) 0%, rgba(191,233,250,.55) 18%, rgba(0,169,236,0) 40%);
  }
  .front-brand {
    position: absolute;
    left: 210px;
    top: 112px;
    color: var(--front-text);
  }
  .front-brand .company {
    font-weight: 700;
    font-size: 46px;
    line-height: 1;
    letter-spacing: .5px;
  }
  .front-brand .company span { display: block; }
  .front-brand .slogan {
    font-size: 14px;
    margin-top: 4px;
  }
  .front-brand .web {
    font-size: 14px;
    margin-top: 22px;
    padding-left: 110px;
  }
  /* Back side */
  .card--back {
    top: 470px;
    background: linear-gradient(160deg, var(--back-light) 0%, var(--back-mid) 100%);
    color: var(--ink);
  }
  .back-brand {
    position: absolute;
    left: 46px;
    top: 92px;
  }
  .back-brand .company {
    font-weight: 700;
    font-size: 34px;
    color: var(--accent-blue);
    line-height: 1;
  }
  .back-brand .slogan {
    font-size: 11px;
    color: var(--ink);
    margin-top: 3px;
    padding-left: 150px;
  }
  .person {
    position: absolute;
    right: 46px;
    top: 152px;
    text-align: right;
  }
  .person .name {
    font-weight: 600;
    font-size: 20px;
    color: var(--accent-blue);
    letter-spacing: .5px;
  }
  .person .title { font-size: 14px; }
  .contacts {
    position: absolute;
    left: 46px;
    top: 232px;
    list-style: none;
    font-size: 15px;
  }
  .contacts li {
    display: flex;
    align-items: center;
    gap: 10px;
    height: 26px;
  }
  .contacts svg { width: 14px; height: 14px; fill: var(--accent-blue); flex: none; }
</style>
</head>
<body>

<section class="card card--front" aria-label="Business card front">
  <div class="front-glow" role="img" aria-label="Soft light-blue decorative band along the left edge"></div>
  <div class="front-brand">
    <p class="company"><span>TOLVIN</span><span>International</span></p>
    <p class="slogan">simple solutions for complex problems</p>
    <p class="web">www.TolvinInternational.com</p>
  </div>
</section>

<section class="card card--back" aria-label="Business card back">
  <div class="back-brand">
    <p class="company">TOLVIN International</p>
    <p class="slogan">simple solutions for complex problems</p>
  </div>
  <div class="person">
    <p class="name">MARLA QUINN</p>
    <p class="title">Sales Manager</p>
  </div>
  <ul class="contacts">
    <li>
      <svg viewBox="0 0 16 16" aria-hidden="true"><rect x="1" y="4" width="14" height="11" rx="2"/><rect x="4" y="1" width="8" height="4" rx="1.5"/></svg>
      +1 (1) 555 010 4471
    </li>
    <li>
      <svg viewBox="0 0 16 16" aria-hidden="true"><path d="M1 3h14v10H1z"/><path d="M1 3l7 6 7-6" fill="none" stroke="#b3e3f8" stroke-width="1.5"/></svg>
      marla@TolvinInternational.com
    </li>
    <li>
      <svg viewBox="0 0 16 16" aria-hidden="true"><circle cx="8" cy="8" r="7"/><path d="M1 8h14M8 1c3 3 3 11 0 14M8 1c-3 3-3 11 0 14" fill="none" stroke="#b3e3f8" stroke-width="1.2"/></svg>
      www.TolvinInternational.com
    </li>
  </ul>
</section>

</body>
</html>
```